Ready to be wowed! Snazzy, sassy, classy Realtor seeking Web banner for unique innovative Realtor!

Placer County Realtor need web banner re-design. Looking for classy, classic, clean design appealing to elite prospects. Previous focus was short sales now looking to gear towards listing and selling homes, remove short sale focus. Must include, license # 07354218, HE logo, phone, email, etc. check out MaraVoss.com for reference info. I am open to suggestions for other needed content for THE BEST WEB BANNER ON EARTH! LOL. I really want to appeal to the upscale clients, also will be getting away from orange colors going more to a green. Please contact me at MaraVossSells@postvale.net for more info
measurements of banner; Images of exactly 960 × 120 pixels will be used as-is. It's Wordpress Genesis.

I'm really looking for something clean that looks upscale and luxury, classy. 

Please update email address to mara@maravoss.com

Reason: I still haven't gotten what I want. I noticed some really good designs closer to the end here, I'm hoping to allow those folks and maybe a few new ones the opportunity to give me exactly what I want! Thanks!

Reason: I still don't have what I want. I want a simple design that shows that I am a Realtor, maybe a picture of a house???? or something related to real estate. Less emphasis on the Harrowgate Estates logo. Classy and upscale. Fonts should be easy to read but not so simply boring. Please, please, please read the brief!! I REALLY want a good banner!!

Please take a look at the site color adjustment. That's what color it will stay. www.MaraVoss.com

Reason: I'm ready to move this to the end now. I need a design. I'm extending hopefully only this last time to take a vote on them. I will be reaching out to a few select designers to make a few modifications. I appreciate everyone's time on this as you know this is a very tough and important decision to make.

Reason: Need more input

Reason: still trying to decide

upscale home sellers

Realtor

• License # 07354218
Phone (916)555-0147
HE LOGO (attached)
areas of service- Roseville, Rocklin, Granite Bay
MaraVossSells@postvale.net

```html
<!DOCTYPE html>
<html lang="en">
<head>
<meta charset="utf-8">
<title>Mara Voss – Realtor Banner</title>
<link rel="stylesheet" href="https://fonts.googleapis.com/css2?family=League+Gothic&family=Oswald:wght@400;500&display=swap">
<style>
  :root {
    --bg: #f6dba5;
    --stripe: #efcf92;
    --green: #6a8a3c;
    --grey: #6f6b66;
    --rule: #c7b080;
    --brand-mark: #1f3f7a;
    --frame: #1a1a1a;
    --photo-top: #8a7a5c;
    --photo-bottom: #3f4a36;
  }
  html, body { margin: 0; padding: 0; overflow: hidden; background: var(--bg); }
  .banner {
    position: relative;
    width: 1200px;
    height: 150px;
    background: var(--bg);
    overflow: hidden;
  }
  .corner-stripes { position: absolute; left: 0; top: 0; }
  .agent-name {
    position: absolute;
    left: 115px;
    top: 2px;
    margin: 0;
    font-family: "League Gothic", "Oswald", sans-serif;
    font-weight: 400;
    font-size: 88px;
    letter-spacing: 2px;
    line-height: 1;
    color: var(--green);
  }
  .agent-phone {
    position: absolute;
    left: 115px;
    top: 106px;
    margin: 0;
    font-family: "Oswald", sans-serif;
    font-weight: 500;
    font-size: 20px;
    letter-spacing: 0.5px;
    color: var(--grey);
  }
  .brokerage {
    position: absolute;
    left: 400px;
    top: 32px;
    display: flex;
    align-items: center;
    gap: 8px;
  }
  .brokerage-mark {
    width: 14px;
    height: 14px;
    background: var(--brand-mark);
  }
  .brokerage-name {
    font-family: "Oswald", sans-serif;
    font-weight: 500;
    font-size: 16px;
    line-height: 1.1;
    color: var(--grey);
    text-transform: uppercase;
  }
  .license {
    position: absolute;
    left: 412px;
    top: 96px;
    margin: 0;
    font-family: "Oswald", sans-serif;
    font-weight: 400;
    font-size: 16px;
    letter-spacing: 0.5px;
    color: var(--grey);
  }
  .service-area {
    position: absolute;
    margin: 0;
    font-family: "Oswald", sans-serif;
    font-weight: 400;
    font-size: 25px;
    line-height: 1;
    color: var(--green);
  }
  .service-area--first { left: 642px; top: 40px; }
  .service-area--second { left: 681px; top: 82px; }
  .service-rule {
    position: absolute;
    height: 1px;
    background: var(--rule);
  }
  .service-rule--first { left: 625px; top: 71px; width: 355px; }
  .service-rule--second { left: 681px; top: 115px; width: 299px; }
  .agent-portrait {
    position: absolute;
    left: 991px;
    top: 10px;
    width: 113px;
    height: 125px;
    border: 2px solid var(--frame);
    background: linear-gradient(180deg, var(--photo-top), var(--photo-bottom));
  }
</style>
</head>
<body>
<div class="banner">
  <svg class="corner-stripes" width="200" height="150" viewBox="0 0 200 150" aria-hidden="true">
    <g stroke="var(--stripe)" stroke-width="1.5">
      <line x1="0" y1="20" x2="20" y2="0"/>
      <line x1="0" y1="34" x2="34" y2="0"/>
      <line x1="0" y1="48" x2="48" y2="0"/>
      <line x1="0" y1="62" x2="62" y2="0"/>
      <line x1="0" y1="110" x2="40" y2="150"/>
      <line x1="0" y1="96" x2="54" y2="150"/>
      <line x1="0" y1="124" x2="26" y2="150"/>
      <line x1="0" y1="138" x2="12" y2="150"/>
    </g>
  </svg>

  <h1 class="agent-name">MARA VOSS</h1>
  <p class="agent-phone">CALL OR TEXT 916.555.0182</p>

  <div class="brokerage">
    <span class="brokerage-mark"></span>
    <span class="brokerage-name">Harrowgate<br>Estates</span>
  </div>
  <p class="license"># 07354218</p>

  <p class="service-area service-area--first">Servicing Roseville</p>
  <div class="service-rule service-rule--first"></div>
  <p class="service-area service-area--second">Rocklin &amp; Granite Bay</p>
  <div class="service-rule service-rule--second"></div>

  <div class="agent-portrait" role="img" aria-label="Portrait photo of the realtor"></div>
</div>
</body>
</html>
```